Cannabis Media Network Advertising Kit

Harbor Bloom Collective is a digital media news network focused on the startups, entrepreneurs and innovative companies in the cannabis industry. We are ready to release our new services for 2017.

We are looking for a modern looking advertising kit created that we would send to our potential clients.

We want it to look similar to our branding. Our website is www.harborbloomcollective.com.

Target Market(s)

Page 3: Audience:
Entrepreneurs, professionals, execs, VC’s, and Investors
Include stats: 34% Female/ 66% Male, 34% 25-34 Years Old $24% 35-44 Years Old

Industry/Entity Type

Media

Font styles to use
Sans Serif

Colors
0555a3
0492cd
ffffff
edf1f7

Requirements
Must have
• Outline Idea is below. Images can be provided.
• Page 1: Header Page (HBC logo)
• Leading digital media news network covering the latest tech, startups, and innovative companies in the cannabis industry.
• Page 2: About Us - Mission and Brand
• Harbor Bloom Collective is the leading digital media platform that is dedicated to profiling the startups, entrepreneurs and innovative companies in the cannabis industry.
• Over the past few years we have been highlighting the upcoming and established businesses in the industry, developed a platform for leaders to share their knowledge and insight, and created
• a spotlight for the innovative technology.
• But most importantly, we have created a community of entrepreneurs, investors and professionals who have the same mission of growing the b2b industry together.
• HBC is more than just a network and brand, we are highlighting history in the making of high quality original content.
• Page 3: Audience:
• Entrepreneurs, professionals, execs, VC’s, and Investors
• Include stats: 34% Female/ 66% Male, 34% 25-34 Years Old $24% 35-44 Years Old
• Page 4: HBC Original Web Series
• Pre/Post Commercial Opportunities $5,000
• Glasshouse Verdicts and HBC Chats
• Glasshouse Verdicts is a un-biased product review segment for the wholesalers, online stores, dispensaries and more.
• HBC Chats: One on one interview with the upcoming and leading founders offering advice and insight for fellow entrepreneurs.
• Page 5: HBC Original Web Series
• Brunch and Botany is a female founder focused web series, where we highlight the leaders, discuss informative topics and latest products.
• Product placement $2,500
• Page 6: HBC Original Web Series
• Behind Doors gives you a peek into the entrepreneur 2.0 and what it is like running a cannabis business.
• See leadership package
• Page 7: Package 1: Foundation $1,000
• 1. Four full platform ads (via QP, VZ, Chirpa, Workmesh, Clipboardly)
• 2. HBC Article/Company Spotlight (One Newsletter feature and full HBC promotion)
• 3. Newsletter Ad (One run, assets provided by client
• Page 8: Package 2: Traction $5,000
• 1. Six full platform ads (via QP, VZ, Chirpa, Workmesh, Clipboardly)
• 4. Business of the Month Badge (HBC Homepage)
• 5. Three Verbal Video Advertisements ( Three segments, up to 10 seconds each)
• Page 9: Package 3: Leadership $15,000
• 5. Three Video Advertisements (Three segments, 30 second commercial)
• 7. Behind Doors Full Segment
• Includes promo and full segment promoted and released via HBC.
• Page 10: Events Promotion
• Event Package $1,000
• 1. Four full platform ads (via QP include QP Event on HBC Page, VZ, Chirpa, Workmesh, Clipboardly)
• A la Carte:
• Add event to HBC calendar, basic promotion via social media $250
• HBCTV Media Sponsor
• Includes co-branded video production of event, exclusive interview with sponsors, and more
• *Cost: To Be Determined
• Page 11: A La Carte
• 1. Event Addition to Calendar (Basic promotion via social media)
• 2. Six full platform ads (via QP, VZ, Chirpa, Workmesh, Clipboardly)
• 3. HBC Article/Company Spotlight (One Newsletter feature and full HBC promotion)
• 4. Newsletter Ad (One run, assets provided by client
• 5. Business of the Month Badge (HBC Homepage)
• 6. Three Verbal Video Advertisements ( Three segments, up to 10 seconds each)
• Page 12: Traction
• Profiled on workmesh, quill dispatch, pageturnr, peoplewall, chirpa, snapgrid
• 10k+ organic email list of professionals
• 16k+ page views increasing 25% each month
• 18k+ social media followers
• Viewed in all 50 states and 98 countries
• Page 13: Message from the CEO
• “We at HBC understand that our industry is different than any other industry out there, we even look at the entrepreneurs and don’t see them just as an entrepreneur but as an entrepreneur 2.0. Why? Because this is the first time in a long time where we have the opportunity to change how an industry is built from the foundation up and each of these individuals are faced with hurdles and challenges we wouldn’t face in any other industry and yet they are doing what it takes to continue to move forward.”
• Page 14: Contact Us
• HBC logo:
• We look forward to growing your brand with the Harbor Bloom Collective! Contact us today at contact@harborbloomcollective.com
Nice to have
• High Res Images from our content. Which we can provide those images, or you can pull from our site and we can send high res after.
Should not have
• Dark Designed.

```html
<!DOCTYPE html>
<html lang="en">
<head>
<meta charset="UTF-8">
<title>Events Promotion — Harbor Bloom Collective</title>
<link href="https://fonts.googleapis.com/css2?family=Open+Sans:wght@400;600&display=swap" rel="stylesheet">
<style>
  :root {
    --brand-deep: #0555a3;
    --brand-bright: #0492cd;
    --brand-mid: #2a7fd0;
    --paper: #edf1f7;
    --white: #ffffff;
    --ink: #3a3a3a;
  }
  html, body {
    margin: 0;
    padding: 0;
    overflow: hidden;
    background: var(--paper);
  }
  .page {
    position: relative;
    width: 1200px;
    height: 900px;
    overflow: hidden;
    background: var(--paper);
    font-family: "Open Sans", Arial, sans-serif;
    color: var(--ink);
  }
  .corner-art, .edge-lines {
    position: absolute;
    top: 0;
    left: 0;
  }
  .section-badge {
    position: absolute;
    left: 47px;
    top: 102px;
    width: 206px;
    height: 206px;
    display: flex;
    align-items: center;
    justify-content: center;
    text-align: center;
    color: var(--brand-deep);
    font-weight: 600;
    font-size: 26px;
    line-height: 1;
    letter-spacing: 0.2px;
  }
  .content {
    position: absolute;
    left: 449px;
    top: 165px;
    width: 700px;
  }
  .package-title {
    margin: 0 0 16px;
    font-weight: 400;
    font-size: 36px;
    line-height: 1.2;
    color: var(--brand-deep);
  }
  .package-list {
    list-style: none;
    margin: 0;
    padding: 0;
    font-size: 19px;
  }
  .package-item {
    margin-bottom: 12px;
    line-height: 34px;
  }
  .package-item .num {
    color: var(--brand-bright);
    font-weight: 600;
  }
  .package-item .detail {
    display: block;
    padding-left: 20px;
  }
  .extras {
    list-style: none;
    margin: 18px 0 0;
    padding: 0;
    font-size: 19px;
  }
  .extras li {
    line-height: 34px;
    margin-bottom: 13px;
    padding-left: 13px;
    text-indent: -13px;
  }
  .extras li::before {
    content: "•";
    color: var(--brand-bright);
    margin-right: 3px;
  }
  .extras sup {
    font-size: 11px;
  }
  .brand-mark {
    position: absolute;
    left: 1095px;
    top: 808px;
    display: flex;
    align-items: center;
    gap: 6px;
    color: var(--brand-deep);
    font-weight: 600;
    font-size: 18px;
  }
  .brand-mark .dot {
    width: 14px;
    height: 14px;
    border-radius: 50%;
    background: var(--brand-bright);
  }
  .page-number {
    position: absolute;
    right: 34px;
    top: 848px;
    font-size: 19px;
    color: var(--ink);
  }
</style>
</head>
<body>
<div class="page">
  <svg class="corner-art" width="1200" height="900" viewBox="0 0 1200 900">
    <defs>
      <linearGradient id="facetBlue" x1="0" y1="0" x2="1" y2="1">
        <stop offset="0" stop-color="#1f6fc4"/>
        <stop offset="0.5" stop-color="#3a95dc"/>
        <stop offset="1" stop-color="#1a63b6"/>
      </linearGradient>
    </defs>
    <g role="img" aria-label="Faceted blue geometric backdrop">
      <polygon points="0,0 276,0 0,405" fill="url(#facetBlue)"/>
      <circle cx="150" cy="205" r="150" fill="var(--white)"/>
      <circle cx="150" cy="205" r="140" fill="url(#facetBlue)"/>
    </g>
    <line x1="276" y1="0" x2="0" y2="405" stroke="var(--white)" stroke-width="6"/>
    <line x1="250" y1="0" x2="0" y2="368" stroke="var(--brand-deep)" stroke-width="4" opacity="0.6"/>
    <circle cx="150" cy="205" r="103" fill="var(--white)"/>
    <line x1="1200" y1="698" x2="1066" y2="900" stroke="var(--brand-bright)" stroke-width="4"/>
    <line x1="1200" y1="745" x2="1097" y2="900" stroke="var(--brand-deep)" stroke-width="3" opacity="0.7"/>
  </svg>

  <div class="section-badge">EVENTS<br>PROMOTION</div>

  <main class="content">
    <h1 class="package-title">Event Package $1,000</h1>
    <ol class="package-list">
      <li class="package-item"><span class="num">1.</span> Four full platform ads
        <span class="detail">(via QP include QP Event on HBC Page, VZ, Chirpa, Workmesh, Clipboardly)</span></li>
      <li class="package-item"><span class="num">2.</span> HBC Article/Company Spotlight
        <span class="detail">(One Newsletter feature and full HBC promotion)</span></li>
      <li class="package-item"><span class="num">3.</span> Newsletter Ad
        <span class="detail">(One run, assets provided by client</span></li>
    </ol>
    <ul class="extras">
      <li>A la Carte:</li>
      <li>Add event to HBC calendar, basic promotion via social media $250</li>
      <li>HBCTV Media Sponsor</li>
      <li>Includes co-branded video production of event, exclusive interview<br>with sponsors, and more</li>
      <li><sup>*</sup>Cost: To Be Determined</li>
    </ul>
  </main>

  <div class="brand-mark"><span class="dot"></span>HBC</div>
  <div class="page-number">10</div>
</div>
</body>
</html>
```